one pager for investors

I will give an initial file in any format needed. Also, the photo that must be included. As well as the logo, that must be the key to the overall design in terms of font, colors, and general layout. I will attach a file in PDF format, which is a one pager presenting a project for investors that I would like to attract and convinced to invest in my project. What I would like you to do is propose me different and better design options, taking my first draft as an example. But you must absolutely keep every single word and number, absolutely all the information written in my first draft(except “ TEMPLATE DRAFT”). Also, on the top left corner is the logo of our company, which I think should be your main inspiration document is a one pager presented to potential investors that not only has to include the most important information in order for them to be able to see everything needed to see the value of the project (which I’ve already taken care of by writing the text needed, numbers presented and timeline shown; all of which which must be preserved in terms of content, but can be completely redesigned and manipulated ) sh a.k.a. Project summary for investor to go for it.
Target Market(s)
Serious rich investors
Industry/Entity Type
Real eatate

```html
<!DOCTYPE html>
<html lang="fr">
<head>
<meta charset="utf-8">
<title>Valmora Properties SA – Projet immobilier XXX</title>
<link rel="stylesheet" href="https://fonts.googleapis.com/css2?family=Montserrat:wght@400;500;600;700&display=swap">
<style>
  :root {
    --backdrop: #a9a9a9;
    --paper: #ffffff;
    --ink: #1f1f22;
    --charcoal: #2b2a2c;
    --royal: #3a56a0;
    --on-dark: #ffffff;
    --on-dark-soft: #d9d9de;
    --on-blue-soft: #dfe5f3;
  }
  * { box-sizing: border-box; margin: 0; padding: 0; }
  html, body {
    width: 1200px; height: 1200px; overflow: hidden;
    background: var(--backdrop);
    font-family: "Montserrat", Arial, sans-serif;
    color: var(--ink);
  }
  .sheet {
    position: absolute; left: 235px; top: 84px;
    width: 730px; height: 1032px;
    background: var(--paper);
  }
  .brand {
    position: absolute; top: 37px; left: 0; width: 100%; height: 73px;
    display: flex; align-items: center; justify-content: center;
  }
  .brand-name {
    font-size: 30px; font-weight: 600; letter-spacing: 3px;
    color: var(--ink); line-height: 1; white-space: nowrap;
  }
  .hero {
    position: absolute; top: 133px; left: 0; width: 100%; height: 312px;
    background:
      linear-gradient(90deg, rgba(70,90,60,.75) 0%, rgba(70,90,60,0) 22%, rgba(0,0,0,0) 78%, rgba(180,100,60,.7) 100%),
      linear-gradient(180deg, #c9ccd2 0%, #b9b5ad 45%, #8e7a68 70%, #5f6a4a 100%);
  }
  .title {
    position: absolute; top: 465px; left: 0; width: 100%;
    text-align: center; font-weight: 700; font-size: 17px; line-height: 22px;
  }
  .description { position: absolute; top: 514px; left: 41px; width: 648px; }
  .description h2 { font-size: 11px; font-weight: 700; line-height: 16px; margin-bottom: 14px; }
  .description p { font-size: 11.2px; line-height: 14.5px; text-align: justify; hyphens: auto; }
  .panel {
    position: absolute; top: 631px; width: 313px; height: 230px;
    padding: 14px 18px; color: var(--on-dark);
  }
  .panel--financial { left: 41px; background: var(--charcoal); }
  .panel--investment { left: 376px; background: var(--royal); padding-left: 21px; }
  .panel h3 { font-size: 14px; font-weight: 600; line-height: 20px; margin-bottom: 13px; }
  .rows { font-size: 11px; line-height: 14.6px; }
  .rows + .rows { margin-top: 14px; }
  .rows.gap-lg { margin-top: 29px; }
  .row { display: grid; grid-template-columns: 156px 1fr; white-space: nowrap; }
  .panel--investment .row { grid-template-columns: 174px 1fr; }
  .row span { font-weight: 400; color: var(--on-dark-soft); }
  .panel--investment .row span { color: var(--on-blue-soft); }
  .row.strong span { font-weight: 700; color: var(--on-dark); }
  .timeline { position: absolute; top: 880px; left: 0; width: 730px; height: 80px; }
  .timeline svg { position: absolute; left: 0; top: 0; }
  .milestone { position: absolute; top: 0; font-size: 11.5px; line-height: 16px; }
  .milestone .date, .milestone .label { position: absolute; left: 0; transform: translateX(-50%); white-space: nowrap; }
  .milestone .date { top: 3px; }
  .milestone .label { top: 59px; }
  .footer {
    position: absolute; top: 978px; left: 72px; width: 585px; height: 28px;
    background: var(--charcoal); color: var(--on-dark);
    font-size: 11.5px; display: flex; align-items: center; justify-content: center;
  }
</style>
</head>
<body>
<main class="sheet">
  <header class="brand">
    <span class="brand-name">VALMORA PROPERTIES SA</span>
  </header>

  <div class="hero" role="img" aria-label="Rendu architectural d'un immeuble résidentiel moderne à terrasses entouré d'arbres"></div>

  <h1 class="title">CONFIDENTIEL – Projet imobilier “XXX”</h1>

  <section class="description">
    <h2>Description du projet</h2>
    <p>Le projet XXX est un projet de dévloppement de 30 appartements de standing en PPE au centre de Lausanne. Le terrain a été sécurisé par la signature du vente à terme conditionnelle. L’objectif est d’obtenir le permis de construire, puis de ventre les lots. Dans un premier temps sur plan puis au fil de la construction. Durée estimée du projet – 24 à 36 mois.</p>
  </section>

  <section class="panel panel--financial">
    <h3>Plan financier</h3>
    <div class="rows">
      <div class="row"><span>Prix du terrain</span><span>CHF 2’000’000</span></div>
      <div class="row"><span>Frais d’acquisition</span><span>CHF 100’000</span></div>
      <div class="row"><span>Coût de construction</span><span>CHF 2’500’000</span></div>
      <div class="row"><span>Divers &amp; imprévus</span><span>CHF 200’000</span></div>
      <div class="row strong"><span>Prix de revient total</span><span>CHF 4’800’000</span></div>
    </div>
    <div class="rows">
      <div class="row strong"><span>Prix de vente total</span><span>CHF 7’500’000</span></div>
      <div class="row"><span>Honoraires sur vente</span><span>CHF 190’000</span></div>
    </div>
    <div class="rows">
      <div class="row strong"><span>Marge projet</span><span>CHF 2’510’000</span></div>
      <div class="row strong"><span>En % sur prix de vente</span><span>33.47%</span></div>
    </div>
  </section>

  <section class="panel panel--investment">
    <h3>Structure d’investissement</h3>
    <div class="rows">
      <div class="row"><span>Besoin de fonds propres</span><span>CHF 2’000’000</span></div>
      <div class="row"><span>Retour de fonds total</span><span>CHF 3’156’600</span></div>
    </div>
    <div class="rows">
      <div class="row strong"><span>Bénéfice net investisseur</span><span>CHF 1’656’600</span></div>
      <div class="row"><span>Soit 2/3 du bénéfice projet</span><span></span></div>
    </div>
    <div class="rows gap-lg">
      <div class="row strong"><span>Multiple sur fonds propres</span><span>x1.83</span></div>
    </div>
    <div class="rows">
      <div class="row strong"><span>Rendement annualisé</span><span>41.4%</span></div>
      <div class="row"><span>Calcul sur 24 mois</span><span></span></div>
    </div>
  </section>

  <section class="timeline">
    <svg width="730" height="80" viewBox="0 0 730 80" aria-hidden="true">
      <line x1="90" y1="40" x2="649" y2="40" stroke="var(--royal)" stroke-width="2.5"/>
      <line x1="112" y1="28" x2="112" y2="52" stroke="var(--royal)" stroke-width="2.5"/>
      <line x1="289" y1="28" x2="289" y2="52" stroke="var(--royal)" stroke-width="2.5"/>
      <line x1="472" y1="28" x2="472" y2="52" stroke="var(--royal)" stroke-width="2.5"/>
      <line x1="631" y1="28" x2="631" y2="52" stroke="var(--royal)" stroke-width="2.5"/>
    </svg>
    <div class="milestone" style="left:112px"><span class="date">08.2024</span><span class="label">Achat parcelle</span></div>
    <div class="milestone" style="left:289px"><span class="date">04.2025</span><span class="label">Mise à l’enquête</span></div>
    <div class="milestone" style="left:472px"><span class="date">12.2025</span><span class="label">Début construction</span></div>
    <div class="milestone" style="left:631px"><span class="date">12.2025</span><span class="label">Livraison</span></div>
  </section>

  <footer class="footer">Valmora Properties Vaud SA - Chemin des Tilleuls 12 - CH-1110 Morges</footer>
</main>
</body>
</html>
```